Metro Fernwick ( New Product Range Office Furniture )

We are looking a dedicated page within our website www.dekvora.com.au ( must be Magento compatible ) to launch our new brand " METRO Fernwick "

We have our existing Brand "ZENO" has been selling in the last 10 years in Australia, We have just manufactured our new range please go our website and type "Metro" in the search box.

The ideal is to have this page to showcase our new products in more professional manner, target audience is corporate customers.

We are also working with a office designers who they will use our website to show their clients with our products

Key Note
This web page is an additional page to be added to our existing website,

so WE DO NOT NEED SHOPPING CART in these pages,

Which means, when customer click on these pages, they will see a total corporate presentation of our Metro Fernwick.

What we want to see is below

We want to showcase each product individually with main image with Long Description, because our product is a modular system we want to add thumbnail images to show 4 more different type of combination images (images to be provided later) so total of 5 images (we can live with 4 images if better spacing when design)

we need a good background theme to make sure they are all match nicely

Hope the above notes will help you get us a better design

Target Market(s)

Corporate End Users, Also Office Interior Designers

Industry/Entity Type

Office Furniture

Number of Pages Required

2 page

Font styles to use
Sans Serif

Requirements
Must have
• Our Metro Fernwick product images ( can get from our website for now )
Nice to have
• Our Product Metro Fernwick Range is a modular system, there are so many configuration that our customer can use to setup their office

```html
<!DOCTYPE html>
<html lang="en">
<head>
<meta charset="utf-8">
<title>Metro Fernwick – New Range</title>
<link rel="stylesheet" href="https://fonts.googleapis.com/css2?family=Open+Sans:wght@400;700&family=Titillium+Web:wght@700&family=Roboto+Condensed:wght@300;400;700&display=swap">
<style>
:root{
  --blue:#0a86cf;
  --grey-head:#7b7f84;
  --text:#2b2b2b;
  --muted:#5f7180;
  --card-bg:#f1f1f1;
  --card-border:#dcdcdc;
  --band:#efefef;
  --white:#ffffff;
  --badge:#a5112a;
  --banner-bg:#eaf4fb;
}
*{box-sizing:border-box;margin:0;padding:0}
html,body{width:1093px;height:1200px;overflow:hidden;background:var(--white);font-family:"Open Sans",sans-serif;color:var(--text)}
.page{position:relative;width:1093px;height:1200px}
.abs{position:absolute}
.card{position:absolute;background:var(--card-bg);border:1px solid var(--card-border);overflow:hidden}
.photo{position:absolute;border-radius:2px}
.photo.cabinet{background:linear-gradient(90deg,#2a2a2a 0 18%,#a59d93 18% 100%)}
.photo.hutch{background:linear-gradient(180deg,#a59d93 0 45%,#3a3a3c 45% 100%)}
.photo.shelf{background:linear-gradient(90deg,#232323 0 10%,#8e8e90 10% 90%,#232323 90%)}
.photo.desk{background:linear-gradient(180deg,#a89e90 0 18%,#2c2c2e 18% 100%)}
.photo.reception{background:linear-gradient(180deg,#c98a4b,#e0b07a)}
.label{position:absolute;background:rgba(255,255,255,.88);border:1px solid #e2e2e2;font-weight:700;font-size:11.5px;letter-spacing:1.8px;line-height:19px;padding:9px 9px;text-transform:uppercase}
.badge{position:absolute;border-radius:50%;background:radial-gradient(circle at 40% 35%,#d02a45,var(--badge));border:2px dashed #fff;color:#fff;font-family:"Roboto Condensed",sans-serif;font-weight:700;text-align:center;display:flex;flex-direction:column;justify-content:center;line-height:1.05;box-shadow:0 0 0 1px var(--badge)}
.btn{position:absolute;background:var(--blue);color:#fff;font-size:11px;display:flex;align-items:center;justify-content:center;width:85px;height:24px}
.section-title{position:absolute;left:78px;font-family:"Titillium Web",sans-serif;font-size:20px;font-weight:700;color:var(--grey-head);text-transform:uppercase}
.section-title .accent{color:var(--blue)}
.section-sub{position:absolute;left:78px;font-size:13px;color:var(--muted)}
.arrows{position:absolute;left:987px;display:flex;gap:6px}
.band{position:absolute;left:0;top:766px;width:1093px;height:434px;background:var(--band)}
.pcard{position:absolute;background:var(--white);border:1px solid var(--card-border);overflow:hidden}
.pcard .name{position:absolute;font-weight:700;font-size:11.5px;letter-spacing:1.8px;line-height:19px;text-transform:uppercase}
</style>
</head>
<body>
<div class="page">

  <!-- hero row -->
  <div class="card" style="left:78px;top:13px;width:217px;height:341px">
    <div class="photo cabinet" role="img" aria-label="Metro Fernwick four drawer filing cabinet" style="left:16px;top:10px;width:150px;height:330px"></div>
    <div class="badge" style="left:152px;top:27px;width:58px;height:58px;font-size:12px"><span>NEW</span><span>COLOUR</span></div>
    <div class="label" style="left:1px;top:264px;width:204px">Metro Fernwick<br>Filing Cabinet&nbsp; 4 Drawers</div>
  </div>

  <div class="card" style="left:318px;top:13px;width:456px;height:341px;background:var(--banner-bg);border-color:#cfe3f1">
    <div class="abs" style="left:0;top:12px;width:100%;text-align:center;font-family:'Roboto Condensed',sans-serif;font-size:25px;font-weight:700;color:#555">Metro Fernwick Now Available</div>
    <div class="abs" style="left:0;top:42px;width:100%;text-align:center;font-family:'Roboto Condensed',sans-serif;font-weight:300;font-size:20px;color:#777">Buy now, pick-up today!*</div>
    <div class="photo hutch" role="img" aria-label="Metro Fernwick office suite with desk, hutch and drawer units" style="left:0;top:78px;width:446px;height:200px"></div>
    <div class="badge" style="left:13px;top:63px;width:96px;height:96px;font-size:21px"><span>NEW</span><span>COLOUR</span></div>
    <div class="abs" style="left:218px;top:318px;width:8px;height:8px;border-radius:50%;background:#555"></div>
    <div class="abs" style="left:231px;top:318px;width:8px;height:8px;border-radius:50%;background:#ccc"></div>
  </div>

  <div class="card" style="left:798px;top:13px;width:216px;height:192px;background:#fbeee0;border-color:#f3e3d1">
    <div class="photo shelf" role="img" aria-label="Metro Fernwick 1500 credenza" style="left:5px;top:34px;width:180px;height:140px"></div>
    <div class="badge" style="left:138px;top:2px;width:46px;height:46px;font-size:10px"><span>NEW</span><span>COLOUR</span></div>
    <div class="label" style="left:70px;top:126px;width:146px;text-align:right">Metro Fernwick<br>1500 Credenza</div>
  </div>

  <div class="card" style="left:798px;top:225px;width:216px;height:129px;background:#ececec">
    <div class="photo reception" role="img" aria-label="Corso curve end reception desk" style="left:0;top:0;width:216px;height:115px;opacity:.85"></div>
    <div class="abs" style="left:10px;top:17px;width:197px;height:94px;background:rgba(255,255,255,.92);text-align:center">
      <div style="margin-top:14px;font-weight:700;font-size:11.5px;letter-spacing:1.8px;line-height:19px">CORSO CURVE END<br>RECEPTION DESK</div>
      <div class="btn" style="left:56px;top:70px">VIEW DETAILS</div>
    </div>
  </div>

  <!-- latest products -->
  <div class="section-title" style="top:383px"><span class="accent">Latest</span> Products</div>
  <div class="section-sub" style="top:420px">Voluptatem accusantium dolorem laudantium, totam rem aperiam</div>
  <svg class="arrows" style="top:426px" width="30" height="12" viewBox="0 0 30 12"><path d="M6 1 1 6l5 5M23 1l5 5-5 5" fill="none" stroke="#333" stroke-width="1.3"/></svg>

  <div class="card" style="left:78px;top:464px;width:217px;height:266px">
    <div class="photo hutch" role="img" aria-label="Metro Fernwick 1800 4-door hutch" style="left:15px;top:12px;width:188px;height:175px"></div>
    <div class="badge" style="left:160px;top:5px;width:42px;height:42px;font-size:9px"><span>NEW</span><span>COLOUR</span></div>
    <div class="label" style="left:0;top:187px;width:190px">Metro Fernwick<br>1800 4-Door Hutch</div>
  </div>
  <div class="card" style="left:318px;top:464px;width:217px;height:266px">
    <div class="photo shelf" role="img" aria-label="Metro Fernwick bookcase" style="left:36px;top:6px;width:120px;height:256px"></div>
    <div class="badge" style="left:163px;top:12px;width:50px;height:50px;font-size:11px"><span>NEW</span><span>COLOUR</span></div>
    <div class="label" style="left:0;top:187px;width:190px">Metro Fernwick<br>1800 4-Door Hutch</div>
  </div>
  <div class="card" style="left:558px;top:464px;width:217px;height:266px">
    <div class="photo cabinet" role="img" aria-label="Metro Fernwick two door cupboard" style="left:28px;top:6px;width:128px;height:256px"></div>
    <div class="badge" style="left:153px;top:14px;width:50px;height:50px;font-size:11px"><span>NEW</span><span>COLOUR</span></div>
    <div class="label" style="left:0;top:187px;width:190px">Metro Fernwick<br>1800 4-Door Hutch</div>
  </div>
  <div class="card" style="left:798px;top:464px;width:217px;height:266px">
    <div class="photo shelf" role="img" aria-label="Metro Fernwick bookcase with cupboard base" style="left:34px;top:10px;width:125px;height:252px"></div>
    <div class="badge" style="left:151px;top:16px;width:50px;height:50px;font-size:11px"><span>NEW</span><span>COLOUR</span></div>
    <div class="label" style="left:0;top:187px;width:190px">Metro Fernwick<br>1800 4-Door Hutch</div>
  </div>

  <!-- popular band -->
  <div class="band"></div>
  <div class="section-title" style="top:795px"><span class="accent">Popular under</span> Metro Fernwick</div>
  <div class="section-sub" style="top:832px">Voluptatem accusantium dolorem laudantium, totam rem aperiam</div>
  <svg class="arrows" style="top:842px" width="30" height="12" viewBox="0 0 30 12"><path d="M6 1 1 6l5 5M23 1l5 5-5 5" fill="none" stroke="#333" stroke-width="1.3"/></svg>

  <div class="pcard" style="left:78px;top:876px;width:296px;height:183px">
    <div class="photo desk" role="img" aria-label="Metro Fernwick 1580 desk" style="left:12px;top:50px;width:144px;height:94px"></div>
    <div class="badge" style="left:121px;top:21px;width:28px;height:28px;font-size:6px"><span>NEW</span><span>COLOUR</span></div>
    <div class="name" style="left:164px;top:55px">Metro Fernwick<br>1580 Desk</div>
    <div class="btn" style="left:165px;top:124px">VIEW DETAILS</div>
  </div>
  <div class="pcard" style="left:398px;top:876px;width:296px;height:183px">
    <div class="photo desk" role="img" aria-label="Metro Fernwick 1580 desk" style="left:12px;top:50px;width:144px;height:94px"></div>
    <div class="badge" style="left:121px;top:21px;width:28px;height:28px;font-size:6px"><span>NEW</span><span>COLOUR</span></div>
    <div class="name" style="left:164px;top:55px">Metro Fernwick<br>1580 Desk</div>
    <div class="btn" style="left:165px;top:124px">VIEW DETAILS</div>
  </div>
  <div class="pcard" style="left:718px;top:876px;width:296px;height:183px">
    <div class="photo desk" role="img" aria-label="Metro Fernwick 1580 desk" style="left:12px;top:50px;width:144px;height:94px"></div>
    <div class="badge" style="left:121px;top:21px;width:28px;height:28px;font-size:6px"><span>NEW</span><span>COLOUR</span></div>
    <div class="name" style="left:164px;top:55px">Metro Fernwick<br>1580 Desk</div>
    <div class="btn" style="left:165px;top:124px">VIEW DETAILS</div>
  </div>

  <div class="pcard" style="left:78px;top:1094px;width:217px;height:120px">
    <div class="photo desk" role="img" aria-label="Metro Fernwick desk" style="left:48px;top:36px;width:122px;height:84px"></div>
    <div class="badge" style="left:141px;top:14px;width:26px;height:26px;font-size:5px"><span>NEW</span><span>COLOUR</span></div>
  </div>
  <div class="pcard" style="left:318px;top:1094px;width:217px;height:120px">
    <div class="photo desk" role="img" aria-label="Metro Fernwick desk" style="left:48px;top:36px;width:122px;height:84px"></div>
    <div class="badge" style="left:141px;top:14px;width:26px;height:26px;font-size:5px"><span>NEW</span><span>COLOUR</span></div>
  </div>
  <div class="pcard" style="left:558px;top:1093px;width:457px;height:120px">
    <div class="photo shelf" role="img" aria-label="Metro Fernwick 1800 open hutch" style="left:18px;top:32px;width:230px;height:90px;background:linear-gradient(180deg,#2a2a2a 0 8%,#8e8e90 8%)"></div>
    <div class="badge" style="left:195px;top:2px;width:48px;height:48px;font-size:10px"><span>NEW</span><span>COLOUR</span></div>
    <div class="name" style="left:297px;top:62px;text-transform:none">Metro Fernwick<br>1800 Open Hutch</div>
  </div>

</div>
</body>
</html>
```